Shopping center investment profile

We need to design a two-page 8.5" x 11" brochure that can be used as a template for profiling our shopping centers and demonstrating our track record to investors.

Our company (KVM Real Estate Investments) owns retail shopping centers in the southwestern United States. Our website is www.kvmtrh.example, but we will be redesigning and modernizing the website and logo in the near future, so please do not use the color schemes or framework of the website for the brochure.

Our investors are institutional and high net worth investors who typically have an existing relationship with our company. They are determining whether to invest multi-millions of dollars in a shopping center opportunity, so the brochure needs to be professional, very high quality and provide key information about the specific property.
Updates

Additional guidance on color scheme:

We would like to see a Blue (something like Hex #5A61BC) and Gold (Hex #EDB215) or (Hex #DDA24B) color scheme with some Black accents 

Thank you!

Target Market(s)

Our target audiences are institutional investors, high net-worth individuals, financial firms and medium to large commercial real estate companies.

Industry/Entity Type

Investment

Requirements
Must have
• Clean and modern look with corresponding fonts and colors.
• Incorporates the information found in the attached "Marlowe Crossing profile" Pages or PDF file.
• Final file design files that can be modified easily
Nice to have
• Two examples of industry brochures are attached. These are examples of the professional quality that we are looking for, not necessarily the design or format.

```html
<!DOCTYPE html>
<html lang="en">
<head>
<meta charset="utf-8">
<title>Marlowe Crossing Property Profile</title>
<link rel="stylesheet" href="https://fonts.googleapis.com/css2?family=Arimo:wght@700&family=Questrial&family=Mulish:wght@600;700&family=Barlow+Condensed:wght@600&display=swap">
<style>
  :root {
    --plum: #86298f;
    --violet: #5b4aa8;
    --indigo: #4b3f9e;
    --slate: #6e6e72;
    --ink: #1d1d22;
    --body: #3c3c44;
    --rule: #c9c9d2;
    --lavender: #9b94d6;
    --dot: #8c88c4;
    --paper: #f7f7f9;
  }
  * { margin: 0; padding: 0; box-sizing: border-box; }
  html, body { width: 887px; height: 1200px; overflow: hidden; background: #fff; }
  .sheet {
    position: relative; width: 887px; height: 1200px; overflow: hidden;
    background: linear-gradient(180deg, #ffffff 0%, var(--paper) 100%);
    font-family: "Questrial", sans-serif; color: var(--body);
  }
  .abs { position: absolute; }

  .title {
    left: 51px; top: 44px; font-family: "Arimo", sans-serif; font-weight: 700;
    font-size: 47px; letter-spacing: -0.5px; white-space: nowrap;
  }
  .title .name-a { color: var(--plum); }
  .title .name-b { color: var(--violet); }
  .title .name-c { color: var(--slate); }

  .tab {
    color: #fff; font-family: "Mulish", sans-serif; font-weight: 700;
    display: flex; align-items: center; padding-left: 16px;
    clip-path: polygon(0 0, 86% 0, 100% 100%, 0 100%);
    border-radius: 3px 0 0 3px;
  }
  .tab-summary { left: 39px; top: 123px; width: 185px; height: 38px; font-size: 21px;
    background: linear-gradient(90deg, var(--plum), #7a2f96); }
  .tab-invest { left: 446px; top: 453px; width: 280px; height: 37px; font-size: 20px;
    background: linear-gradient(90deg, var(--indigo), #5f52b4); }

  .summary {
    left: 39px; top: 168px; width: 392px; height: 215px;
    border: 2px solid #8a3b98; border-radius: 4px; padding: 4px 16px 0 16px; background: #fff;
  }
  .summary .row, .invest .row {
    display: flex; justify-content: space-between; align-items: center;
    height: 29.4px; border-bottom: 1px solid var(--rule); font-size: 13.5px;
  }
  .summary .row:last-child { border-bottom: none; }
  .summary .label { color: var(--violet); font-family: "Mulish", sans-serif; font-weight: 700; }
  .summary .value, .invest .value { color: var(--ink); font-family: "Mulish", sans-serif; font-weight: 600; }

  .heading-opp {
    left: 459px; top: 117px; width: 389px; padding-bottom: 4px;
    border-bottom: 1.5px solid #a8a1d8; color: var(--plum);
    font-family: "Mulish", sans-serif; font-weight: 700; font-size: 20px;
  }
  .opportunity { left: 459px; top: 160px; width: 392px; list-style: none; }
  .opportunity li {
    position: absolute; left: 0; width: 376px; padding-left: 15px;
    font-size: 13px; line-height: 14.6px; color: var(--body);
  }
  .opportunity li::before {
    content: ""; position: absolute; left: 1px; top: 4px; width: 6px; height: 6px;
    border-radius: 50%; background: var(--dot);
  }

  .heading-results { left: 39px; top: 434px; color: var(--violet);
    font-family: "Mulish", sans-serif; font-weight: 700; font-size: 19px; }
  .results { left: 39px; top: 472px; width: 392px; list-style: none; }
  .results li { position: absolute; left: 0; display: flex; gap: 6px; width: 382px;
    font-size: 13px; line-height: 14.6px; }
  .results svg { flex: 0 0 18px; margin-top: 1px; }

  .address { left: 39px; top: 664px; font-family: "Barlow Condensed", sans-serif; font-weight: 600;
    font-size: 35px; line-height: 42px; color: var(--slate); letter-spacing: 0.3px; }

  .url-tab { left: 39px; top: 774px; width: 266px; height: 37px; font-family: "Questrial", sans-serif;
    font-weight: 400; font-size: 16px; letter-spacing: 1.6px; gap: 7px; padding-left: 16px;
    white-space: nowrap;
    background: linear-gradient(90deg, var(--plum), #7a2f96); }

  .invest {
    left: 446px; top: 499px; width: 392px; height: 302px;
    border: 2px solid #5446a8; border-radius: 4px; padding: 4px 16px 0 16px; background: #fff;
  }
  .invest .row { height: 31px; font-size: 13px; }
  .invest .label { color: var(--ink); font-family: "Mulish", sans-serif; font-weight: 600; }
  .invest .total-row { height: 44px; border-bottom: 1px solid var(--rule); padding: 4px 8px 4px 8px; }
  .invest .total {
    height: 36px; background: var(--lavender); color: #fff; font-size: 13px;
    display: flex; align-items: center; padding-left: 17px; font-family: "Mulish", sans-serif; font-weight: 600;
  }
  .invest .structure { border-bottom: none; align-items: flex-start; height: auto; padding-top: 8px; }
  .invest .structure ul { list-style: none; font-family: "Mulish", sans-serif; font-weight: 600;
    color: var(--ink); line-height: 15.5px; }
  .invest .structure li::before { content: "• "; }

  .band-top { left: 0; top: 817px; width: 887px; height: 6px; background: linear-gradient(90deg, var(--violet), #3f3a9a); }
  .storefront {
    left: 0; top: 829px; width: 887px; height: 356px;
    background: linear-gradient(180deg, #7fb4e0 0%, #b9d4ea 30%, #d9a374 52%, #b24a32 62%, #8e8a88 80%, #6d6a6c 100%);
  }
  .band-bottom { left: 0; top: 1185px; width: 887px; height: 15px; background: #7b2f96; }
</style>
</head>
<body>
<main class="sheet">
  <h1 class="abs title"><span class="name-a">Marlowe</span> <span class="name-b">Crossing</span> <span class="name-c">Property Profile</span></h1>

  <div class="abs tab tab-summary">Summary</div>
  <section class="abs summary">
    <div class="row"><span class="label">Property Type</span><span class="value">Shopping Center</span></div>
    <div class="row"><span class="label">Size</span><span class="value">79,490 sq ft</span></div>
    <div class="row"><span class="label">Purchased</span><span class="value">April 2011</span></div>
    <div class="row"><span class="label">Total Investment</span><span class="value">$X,XXX,XXX</span></div>
    <div class="row"><span class="label">Purchase Occupancy</span><span class="value">8.39%</span></div>
    <div class="row"><span class="label">Current Occupancy</span><span class="value">97.29%</span></div>
    <div class="row"><span class="label">Projected 5-year IRR (Unleveraged)</span><span class="value">XX.XX%</span></div>
  </section>

  <h2 class="abs heading-opp">Opportunity</h2>
  <ul class="abs opportunity">
    <li style="top:0">Bank owned property with attractive purchase price</li>
    <li style="top:30px">Strong relationship with seller’s broker and decision makers</li>
    <li style="top:76px">Redevelopment upside with management and leasing</li>
    <li style="top:107px">No major renovations required</li>
    <li style="top:137px">Redmesa location has very strong population, education and income demographics</li>
    <li style="top:183px">Adjacent to premier 2,500-residence master planned community of Sable Creek Lakes</li>
    <li style="top:229px">Strong employment area with the new Halvern Gateway hospital and the adjacent Corwin Hale Cancer center</li>
  </ul>

  <h2 class="abs heading-results">Results</h2>
  <ul class="abs results">
    <li style="top:0"><svg width="18" height="16" viewBox="0 0 18 16"><rect x="1" y="4" width="11" height="11" fill="none" stroke="#5b4aa8" stroke-width="1.6"/><path d="M3.5 9 L7 12.5 L16.5 1.5" fill="none" stroke="#5b4aa8" stroke-width="2.4" stroke-linecap="round"/></svg><span>Stabilized the shopping center within three years, producing excellent results for investors</span></li>
    <li style="top:46px"><svg width="18" height="16" viewBox="0 0 18 16"><rect x="1" y="4" width="11" height="11" fill="none" stroke="#5b4aa8" stroke-width="1.6"/><path d="M3.5 9 L7 12.5 L16.5 1.5" fill="none" stroke="#5b4aa8" stroke-width="2.4" stroke-linecap="round"/></svg><span>Transformed the center into a vibrant destination that the surrounding community is excited about</span></li>
    <li style="top:92px"><svg width="18" height="16" viewBox="0 0 18 16"><rect x="1" y="4" width="11" height="11" fill="none" stroke="#5b4aa8" stroke-width="1.6"/><path d="M3.5 9 L7 12.5 L16.5 1.5" fill="none" stroke="#5b4aa8" stroke-width="2.4" stroke-linecap="round"/></svg><span>Transitioned legacy tenants to upgrade the business operators</span></li>
    <li style="top:139px"><svg width="18" height="16" viewBox="0 0 18 16"><rect x="1" y="4" width="11" height="11" fill="none" stroke="#5b4aa8" stroke-width="1.6"/><path d="M3.5 9 L7 12.5 L16.5 1.5" fill="none" stroke="#5b4aa8" stroke-width="2.4" stroke-linecap="round"/></svg><span>Reduced the shopping center’s operating expenses by replacing vendors and appealing property taxes</span></li>
  </ul>

  <p class="abs address">SWC OF HARLAN RD AND<br>COPPER RD REDMESA, ARIZONA</p>

  <div class="abs tab url-tab"><svg width="12" height="12" viewBox="0 0 12 12"><circle cx="6" cy="6" r="5" fill="none" stroke="#fff" stroke-width="1"/><ellipse cx="6" cy="6" rx="2.2" ry="5" fill="none" stroke="#fff" stroke-width="0.9"/><path d="M1 6 H11 M2 3.5 H10 M2 8.5 H10" stroke="#fff" stroke-width="0.8"/></svg><span>www.kvmtrh.example</span></div>

  <div class="abs tab tab-invest">Investment Information</div>
  <section class="abs invest">
    <div class="row"><span class="label">Purchase Price</span><span class="value">$X,XXX,XXX</span></div>
    <div class="row"><span class="label">Sponsor Acquisition Fee</span><span class="value">$XX,XXX</span></div>
    <div class="row"><span class="label">Painting and Landscape</span><span class="value">$XXX,XXX</span></div>
    <div class="row"><span class="label">TI/LC Reserve</span><span class="value">$X,XXX,XXX</span></div>
    <div class="row"><span class="label">Operating Expenses</span><span class="value">$XXX,XXX</span></div>
    <div class="total-row"><div class="total">Total Cash Investment</div></div>
    <div class="row"><span class="label">Investor / Sponsor Split</span><span class="value">XX% / XX%</span></div>
    <div class="row structure"><span class="label">Structure</span>
      <ul><li>Cash Flow Pari Passu</li><li>Acquisition Fee</li><li>Management Fee</li></ul>
    </div>
  </section>

  <div class="abs band-top"></div>
  <div class="abs storefront" role="img" aria-label="Rendering of the shopping center storefronts with signage, trees and parked cars under a blue sky"></div>
  <div class="abs band-bottom"></div>
</main>
</body>
</html>
```